yourSmileCare Brookvale Business Card

Please design a two sided business card that is Elegant and Professional
Add subtle elegant patterns to suit Spot UV printing/ or raised printing

Name: Dr Marcus T. Fenwick
Qualification: BDSc (QLD)
Title: Dental Surgeon, Clinical Director
Company: yourSmileCare Brookvale
Phone: (02) 7593 2268
Address: Shop 7/18-20 Lindon Ave Brookvale 2097
email: info@yoursmilecarebrookvale.com.au
Facebook: linkvue.com/yoursmilecarebrookvale

Motto:
Quality dentistry you can trust

Description of services (not compulsory):
Preventative Dentistry | General Dentistry
Cosmetic Dentistry | Teeth Whitening
Crown and Bridge | Root Canal Therapy
Veneers | Clearvono | Orthodontics
Emergency Dental Care | After Hours

Personalised Treatment Plans
Transparent Fees

Please make sure card is elegant and professional

Target Market(s)

general population, patients,
Dental sales companies, other professions

Industry/Entity Type

Dental Clinic

Contact Information for Business Card

Name: Dr Marcus T. Fenwick
Qualification: BDSc (QLD)
Phone: (02) 7593 2268
Address: Shop 7/18-20 Lindon Ave Brookvale

Motto:

Description of services (not compulsory)

Transparent Fees

Image of dental surgery optional

Please make sure card is elegant and profession

Requirements
Must have
• Logo
• Name, Title (next to name), Business
• Phone, address, facbeook
• Must have stylish design to suit SPOT UV reflective printing
Nice to have
• Subtle elegant patterns which will have Spot UV on them when printed
• Colours to match logo colour
• Description of services
Should not have
• Small fonts that are hard to read
• DO NOT PUT IMAGES OF DENTAL INSTRUMENTS OR TEETH PLEASE

```html
<!DOCTYPE html>
<html lang="en">
<head>
<meta charset="utf-8">
<title>yourSmileCare Brookvale Business Card</title>
<link rel="stylesheet" href="https://fonts.googleapis.com/css2?family=Montserrat:wght@600&family=Open+Sans:wght@400;600;700&display=swap">
<style>
  :root {
    --backdrop: #2b2b2b;
    --green-light: #bcdc62;
    --green-mid: #a6cf48;
    --green-deep: #8cbf34;
    --green-text: #8dc63f;
    --grey-text: #6f6f6f;
    --grey-soft: #8a8a8a;
    --white: #ffffff;
    --paper: #ffffff;
  }
  * { box-sizing: border-box; margin: 0; padding: 0; }
  html, body {
    width: 1200px; height: 900px; overflow: hidden;
    background: var(--backdrop);
    font-family: "Open Sans", Arial, sans-serif;
  }
  .stage {
    width: 1200px; height: 900px;
    display: flex; flex-direction: column;
    align-items: center; justify-content: center; gap: 40px;
  }
  .card {
    position: relative;
    width: 620px; height: 379px;
    border-radius: 18px;
    overflow: hidden;
  }

  /* Contact side */
  .card--contact {
    background: radial-gradient(ellipse at 45% 45%, var(--green-light) 0%, var(--green-mid) 55%, var(--green-deep) 100%);
    color: var(--white);
  }
  .card--contact .divider {
    position: absolute; left: 300px; top: 140px;
    width: 1px; height: 95px;
    background: linear-gradient(to bottom, rgba(255,255,255,0), rgba(120,170,40,0.9) 40%, rgba(120,170,40,0));
  }
  .card--contact .brand {
    position: absolute; left: 36px; top: 250px;
    display: flex; align-items: center; gap: 10px;
  }
  .brand-dot {
    width: 16px; height: 16px; border-radius: 50%;
    background: var(--white);
  }
  .brand-name {
    font-family: "Montserrat", "Open Sans", sans-serif;
    font-weight: 600; font-size: 25px; letter-spacing: -0.3px;
    color: var(--white);
  }
  .identity {
    position: absolute; left: 318px; top: 46px;
  }
  .identity .name { font-weight: 700; font-size: 18px; }
  .identity .qual { font-weight: 400; font-size: 15px; }
  .identity .role {
    margin-top: 6px;
    font-size: 11.5px; color: rgba(80,110,30,0.85);
  }
  .contacts {
    position: absolute; left: 318px; top: 150px;
    list-style: none;
    display: flex; flex-direction: column; gap: 7px;
    font-size: 12.5px;
  }
  .contacts li { display: flex; align-items: center; gap: 9px; }
  .contacts svg { width: 15px; height: 15px; flex: none; }

  /* Services side */
  .card--services {
    background: var(--paper);
    text-align: center;
  }
  .card--services .brand {
    position: absolute; left: 0; right: 0; top: 70px;
    display: flex; align-items: center; justify-content: center; gap: 12px;
  }
  .card--services .brand-dot { background: var(--green-text); width: 20px; height: 20px; }
  .card--services .brand-name { color: var(--green-text); font-size: 34px; }
  .services {
    position: absolute; left: 0; right: 0; top: 200px;
  }
  .services h2 {
    display: inline-block;
    font-size: 17px; font-weight: 700;
    color: var(--grey-text);
    border-bottom: 1.5px solid var(--grey-text);
    line-height: 1.2; margin-bottom: 14px;
  }
  .services ul { list-style: none; }
  .services li {
    font-size: 15.5px; color: var(--green-text);
    line-height: 1.55;
  }
  .services .bullet { color: var(--grey-soft); font-size: 12px; margin: 0 3px; }
</style>
</head>
<body>
<main class="stage">

  <section class="card card--contact" aria-label="Business card contact side">
    <div class="divider"></div>
    <div class="brand">
      <span class="brand-dot"></span>
      <span class="brand-name">yourSmileCare Brookvale</span>
    </div>
    <div class="identity">
      <p><span class="name">Dr Marcus T. Fenwick,</span> <span class="qual">BDSc (QLD)</span></p>
      <p class="role">Dental Surgeon, Clinical Director</p>
    </div>
    <ul class="contacts">
      <li>
        <svg viewBox="0 0 16 16" aria-hidden="true"><circle cx="8" cy="8" r="7" fill="none" stroke="#fff" stroke-width="1.3"/><path d="M5.4 4.6c.4-.3.8-.2 1 .2l.6 1.1c.2.3.1.6-.2.8l-.4.3c.4.9 1 1.5 1.9 1.9l.3-.4c.2-.3.5-.4.8-.2l1.1.6c.4.2.5.6.2 1-.6.9-1.4 1.1-2.3.7-1.7-.8-2.9-2-3.6-3.6-.4-.9-.2-1.7.6-2.4z" fill="#fff"/></svg>
        <span>(02) 7593 2268</span>
      </li>
      <li>
        <svg viewBox="0 0 16 16" aria-hidden="true"><rect x="1.5" y="3.5" width="13" height="9" fill="none" stroke="#fff" stroke-width="1.3"/><path d="M1.5 3.5 8 9l6.5-5.5" fill="none" stroke="#fff" stroke-width="1.3"/></svg>
        <span>info@yoursmilecarebrookvale.com.au</span>
      </li>
      <li>
        <svg viewBox="0 0 16 16" aria-hidden="true"><rect x="1.5" y="1.5" width="13" height="13" rx="1.5" fill="#fff"/></svg>
        <span>linkvue.com/yoursmilecarebrookvale</span>
      </li>
      <li>
        <svg viewBox="0 0 16 16" aria-hidden="true"><circle cx="8" cy="8" r="7" fill="none" stroke="#fff" stroke-width="1.3"/><path d="M8 3.8c-1.6 0-2.7 1.2-2.7 2.6 0 1.9 2.7 5 2.7 5s2.7-3.1 2.7-5c0-1.4-1.1-2.6-2.7-2.6z" fill="#fff"/><circle cx="8" cy="6.4" r="1" fill="#a6cf48"/></svg>
        <span>Shop 7/18-20 Lindon Ave Brookvale</span>
      </li>
    </ul>
  </section>

  <section class="card card--services" aria-label="Business card services side">
    <div class="brand">
      <span class="brand-dot"></span>
      <span class="brand-name">yourSmileCare Brookvale</span>
    </div>
    <div class="services">
      <h2>Services</h2>
      <ul>
        <li><span class="bullet">●</span>Preventative Dentistry <span class="bullet">●</span>General Dentistry</li>
        <li><span class="bullet">●</span>Teeth Whitening Crown and Bridge <span class="bullet">●</span>Root Canal Therapy Veneers</li>
        <li><span class="bullet">●</span>Cosmetic Dentistry <span class="bullet">●</span>Clearvono <span class="bullet">●</span>Orthodontics Emergency Dental Care</li>
      </ul>
    </div>
  </section>

</main>
</body>
</html>
```